I need a design for Corvane Homes which is a custom home builder. The name on it will be Dan Hartley, and I will give the phone number to the winning design. No address or website needed.

```html
<!DOCTYPE html>
<html lang="en">
<head>
<meta charset="utf-8">
<title>Corvane Homes — Business Card, Dan Hartley</title>
<link href="https://fonts.googleapis.com/css2?family=Arvo:wght@400;700&display=swap" rel="stylesheet">
<style>
  :root {
    --backdrop: #d6d6d8;
    --brand-blue: #2e3184;
    --brand-blue-soft: #3d4091;
    --brand-blue-faint: rgba(255, 255, 255, 0.07);
    --lavender-faint: #e6e6f0;
    --grey-rule: #dcdcdc;
    --card-white: #ffffff;
    --ink-white: #ffffff;
  }
  * { box-sizing: border-box; margin: 0; padding: 0; }
  html, body {
    width: 1200px;
    height: 985px;
    overflow: hidden;
    background: var(--backdrop);
    font-family: "Arvo", Georgia, serif;
  }
  .stage {
    position: relative;
    width: 1200px;
    height: 985px;
  }
  .card {
    position: absolute;
    left: 285px;
    width: 630px;
    height: 360px;
    border-radius: 22px;
    overflow: hidden;
    box-shadow: 0 6px 18px rgba(0, 0, 0, 0.18);
  }
  .card--back {
    top: 80px;
    background: var(--card-white);
  }
  .card--front {
    top: 540px;
    background: var(--brand-blue);
  }

  /* faint background texture area */
  .texture {
    position: absolute;
    left: 0;
    top: 0;
    width: 440px;
    height: 100%;
  }
  .card--back .texture {
    background: linear-gradient(120deg, var(--lavender-faint) 0%, rgba(230, 230, 240, 0.55) 45%, rgba(255, 255, 255, 0) 85%);
  }
  .card--front .texture {
    background: linear-gradient(120deg, rgba(255, 255, 255, 0.09) 0%, rgba(255, 255, 255, 0.05) 45%, rgba(255, 255, 255, 0) 85%);
  }

  /* paired thin rules */
  .rule {
    position: absolute;
    left: 0;
    width: 460px;
    height: 2px;
  }
  .card--back .rule { background: var(--grey-rule); }
  .card--front .rule { background: var(--brand-blue-soft); }
  .rule--a { top: 118px; }
  .rule--b { top: 126px; }
  .rule--c { top: 196px; }
  .rule--d { top: 204px; }

  /* brand lockup: plain circle + wordmark */
  .brand {
    position: absolute;
    right: 48px;
    display: flex;
    align-items: center;
    gap: 14px;
  }
  .brand__dot {
    width: 34px;
    height: 34px;
    border-radius: 50%;
  }
  .brand__name {
    font-size: 30px;
    font-weight: 400;
    letter-spacing: 1px;
    text-transform: uppercase;
    white-space: nowrap;
  }
  .card--back .brand { bottom: 96px; }
  .card--back .brand__dot { background: var(--brand-blue); }
  .card--back .brand__name { color: var(--brand-blue); }
  .card--front .brand { bottom: 70px; }
  .card--front .brand__dot { background: var(--ink-white); }
  .card--front .brand__name { color: var(--ink-white); }

  /* name tab on the back */
  .name-tab {
    position: absolute;
    right: 0;
    bottom: 0;
    width: 250px;
    height: 50px;
    background: var(--brand-blue);
    border-top-left-radius: 22px;
    display: flex;
    align-items: center;
    justify-content: center;
    color: var(--ink-white);
    font-size: 22px;
    font-weight: 700;
    letter-spacing: 2px;
  }

  /* contact block on the front */
  .contact {
    position: absolute;
    left: 150px;
    top: 104px;
    color: var(--ink-white);
  }
  .contact__name {
    font-size: 26px;
    font-weight: 700;
    letter-spacing: 2px;
    margin-bottom: 10px;
  }
  .contact__phone {
    display: flex;
    align-items: center;
    gap: 10px;
    font-size: 20px;
    letter-spacing: 2px;
  }
  .contact__icon {
    width: 22px;
    height: 22px;
    flex: none;
  }
</style>
</head>
<body>
<main class="stage">

  <section class="card card--back" aria-label="Card back">
    <div class="texture" role="img" aria-label="Faint lavender background texture"></div>
    <div class="rule rule--a"></div>
    <div class="rule rule--b"></div>
    <div class="rule rule--c"></div>
    <div class="rule rule--d"></div>
    <div class="brand">
      <span class="brand__dot"></span>
      <span class="brand__name">Corvane Homes</span>
    </div>
    <div class="name-tab">Dan Hartley</div>
  </section>

  <section class="card card--front" aria-label="Card front">
    <div class="texture" role="img" aria-label="Faint tonal background texture"></div>
    <div class="rule rule--c"></div>
    <div class="rule rule--d"></div>
    <div class="contact">
      <p class="contact__name">Dan Hartley</p>
      <p class="contact__phone">
        <svg class="contact__icon" viewBox="0 0 24 24" aria-hidden="true">
          <rect x="0" y="0" width="24" height="24" rx="4" fill="#ffffff"/>
          <path d="M8.2 5.5c.4-.3 1-.2 1.3.2l1.5 2.2c.3.4.2 1-.2 1.3l-.9.7c.6 1.6 1.9 3.3 3.4 4.3l.8-.8c.4-.4 1-.4 1.3 0l1.8 1.9c.4.4.3 1-.1 1.3l-1.3 1c-.8.6-1.9.6-2.8.1-2.8-1.6-5-4.4-6-7.4-.3-1-.1-2 .6-2.7z" fill="#2e3184"/>
        </svg>
        <span>000 000 000</span>
      </p>
    </div>
    <div class="brand">
      <span class="brand__dot"></span>
      <span class="brand__name">Corvane Homes</span>
    </div>
  </section>

</main>
</body>
</html>
```